Stationary and design update for my brand

I need new letterhead, a new business card, business envelope design, new keynote and powerpoint branded slides (16x9). I have logo samples in various styles and brand standards for fonts and colors.

Font styles to use
Sans Serif

```html
<!DOCTYPE html>
<html lang="en">
<head>
<meta charset="utf-8">
<title>Ridgeline Coaching – Brand Stationery &amp; Slides</title>
<link rel="stylesheet" href="https://fonts.googleapis.com/css2?family=Roboto+Slab:wght@300;700&family=Jost:wght@400&family=Arimo:wght@400&display=swap">
<style>
:root{
  --orange:#f7931e;
  --grey:#4d4d4d;
  --paper:#f4f2f2;
  --white:#ffffff;
  --board:#000000;
  --label:#ffffff;
  --text:#555555;
  --slab:"Roboto Slab",serif;
  --sans:"Jost",sans-serif;
  --body:"Arimo",sans-serif;
}
*{margin:0;padding:0;box-sizing:border-box}
html,body{width:1200px;height:1062px;overflow:hidden;background:var(--board)}
.board{position:relative;width:1200px;height:1062px;background:var(--board);font-family:var(--sans);color:var(--text)}
.item{position:absolute;overflow:hidden}
.label{position:absolute;color:var(--label);font-family:var(--sans);font-size:7px;transform:translateX(-50%);white-space:nowrap}

/* plain brand bands */
.band{position:absolute;left:0;bottom:0;width:100%;background:var(--grey);border-top:4px solid var(--orange)}
.band-white{background:var(--white);border-top-color:var(--grey)}

.brand{font-family:var(--slab);font-weight:300;color:var(--orange);line-height:1;letter-spacing:.02em;white-space:nowrap}
.brand-sub{font-family:var(--sans);font-size:3.4px;letter-spacing:.03em;color:var(--grey);margin-top:2px;text-transform:uppercase;white-space:nowrap}
.on-dark{color:var(--white)}
.contact{position:absolute;left:0;right:0;text-align:center;color:var(--white);font-family:var(--sans);white-space:nowrap}
.contact .ico{display:inline-block;width:3px;height:4px;background:var(--orange);margin:0 2px 0 4px;vertical-align:middle}

/* business card */
.card-front{left:104px;top:218px;width:230px;height:131px;background:var(--paper)}
.card-front .name{position:absolute;top:15px;width:100%;text-align:center;font-family:var(--slab);font-weight:700;font-size:8.5px;color:var(--orange)}
.card-front .name small{font-size:5px}
.card-front .roles{position:absolute;top:28px;width:100%;text-align:center;font-size:5.2px;color:var(--grey)}
.card-front .band{height:44px}
.card-back{left:102px;top:380px;width:230px;height:131px;background:var(--grey);display:flex;flex-direction:column;align-items:center;justify-content:center}
.card-back .brand{color:#3a3a3a;font-size:28px}
.card-back .brand-sub{color:#3a3a3a;font-size:5.2px}

/* letterhead */
.letterhead{left:354px;top:80px;width:313px;height:442px;background:var(--paper)}
.letterhead .logo{position:absolute;left:24px;top:40px}
.letterhead .logo .brand{font-size:17px}
.letterhead .greeting{position:absolute;left:24px;top:123px;font-family:var(--body);font-size:8.5px;color:var(--grey)}
.letterhead .body{position:absolute;left:24px;top:148px;width:266px;font-family:var(--body);font-size:4.7px;line-height:7.4px;color:#666;text-align:justify}
.letterhead .body p{margin-bottom:7.4px}
.letterhead .closing{position:absolute;left:24px;top:308px;font-family:var(--body);font-size:5px;color:#666}
.letterhead .signer{position:absolute;left:24px;top:351px;font-family:var(--body);font-size:7px;color:var(--grey)}
.letterhead .signer small{display:block;font-size:5px;margin-top:1px}
.letterhead .band{height:36px}

/* notepads */
.pad{top:59px;width:131px;height:195px}
.pad .rings{position:absolute;top:0;left:6px;right:6px;height:6px;background:repeating-linear-gradient(90deg,#222 0 1.2px,transparent 1.2px 6.2px)}
.pad .logo{position:absolute;top:44px;width:100%;text-align:center}
.pad .logo .brand{font-size:18px}
.pad .band{height:56px}
.pad .url{position:absolute;left:0;right:0;bottom:16px;text-align:center;font-size:5.5px;color:var(--orange)}
.pad-white{left:700px;background:var(--white)}
.pad-orange{left:847px;background:var(--orange)}
.pad-lined{left:993px;background:var(--white)}
.pad-lined .logo{top:24px}
.pad-lined .logo .brand{font-size:13px}
.pad-lined .url{bottom:8px}
.pad-lined .lines{position:absolute;left:14px;right:12px;top:52px;height:124px;background:repeating-linear-gradient(180deg,transparent 0 9.5px,#cfcfcf 9.5px 10px)}

/* envelope */
.env-back{left:759px;top:279px;width:352px;height:160px;background:var(--paper)}
.env-back .flap{position:absolute;left:0;top:0;width:100%;height:58px;background:var(--orange);border-radius:0 0 28px 28px}
.env-back .flap span{position:absolute;top:26px;width:100%;text-align:center;color:var(--white);font-size:6px}
.env-front{left:711px;top:363px;width:352px;height:160px;background:var(--paper)}
.env-front .logo{position:absolute;left:15px;top:16px}
.env-front .logo .brand{font-size:18px}
.env-front .band{height:34px}
.env-front .addr{position:absolute;right:55px;bottom:9px;color:var(--white);font-size:5.8px;text-align:center;line-height:7.5px;white-space:nowrap}

/* slides */
.slide{width:328px;height:184px;background:var(--white)}
.slide .footer{position:absolute;left:0;bottom:0;width:100%;height:7px;background:var(--orange);color:var(--white);font-size:4.2px;letter-spacing:.2em;line-height:7px;padding:0 24px}
.slide .footer b{position:absolute;right:26px;font-weight:400}
.slide .head{position:absolute;left:0;top:0;width:100%;height:41px;background:var(--grey);border-bottom:3px solid var(--orange)}
.slide .title{position:absolute;left:20px;top:12px;font-family:var(--slab);font-weight:700;font-size:10px;color:var(--orange)}
.slide .subtitle{position:absolute;left:20px;top:26px;font-size:6.5px;color:var(--white)}
.slide .slide-logo{position:absolute;right:20px;top:13px;text-align:center}
.slide .slide-logo .brand{font-size:11px}
.slide .slide-logo .brand-sub{font-size:2.6px;color:var(--white)}
.slide .para{font-family:var(--body);font-size:3.5px;line-height:5.2px;color:#555;text-align:justify}
.slide h4{font-family:var(--body);font-weight:400;font-size:5.6px;color:var(--orange);margin:5px 0 2px}

.slide-title{left:108px;top:563px;background:var(--grey)}
.slide-title .sky{position:absolute;left:0;top:0;width:100%;height:112px;background:linear-gradient(180deg,#6b5870 0%,#b86e63 35%,#8a7b86 70%,#46495a 100%);border-bottom:4px solid var(--orange)}
.slide-title .slide-logo{right:20px;top:38px}
.slide-title .slide-logo .brand{font-size:22px}
.slide-title .slide-logo .brand-sub{font-size:4px}
.slide-title .welcome{position:absolute;left:0;width:301px;top:128px;text-align:center;color:var(--white)}
.slide-title .welcome .l1{font-size:14px;line-height:15px}
.slide-title .welcome .l2{font-family:var(--slab);font-weight:700;font-size:12px;line-height:14px}
.slide-title .welcome .l3{font-size:13px;line-height:14px}

.slide-team{left:451px;top:563px}
.slide-team .title{color:var(--white)}
.member{position:absolute;top:52px;width:52px}
.member .photo{width:52px;height:52px;background:var(--grey);border:1.5px solid #e6e6e6;color:#ccc;font-size:6px;display:flex;align-items:center;justify-content:center}
.member .mname{font-family:var(--body);font-size:5px;color:var(--orange);margin-top:8px}
.member .mtitle{font-family:var(--body);font-size:4.8px;color:#888;margin-top:2px}
.member .para{margin-top:5px;font-size:3.2px;line-height:4.6px}

.slide-meet{left:795px;top:563px}
.slide-meet .photo-area{position:absolute;left:17px;top:52px;width:138px;height:112px;background:linear-gradient(135deg,#c9d6e3 0%,#7e8ea3 45%,#3c4657 100%)}
.slide-meet .copy{position:absolute;left:173px;top:48px;width:137px}

.slide-chart{left:108px;top:770px}
.slide-chart .chart{position:absolute;left:20px;top:54px;width:105px;height:78px}
.slide-chart .copy{position:absolute;left:157px;top:54px;width:153px}
.slide-chart .copy .para{margin-bottom:5px}
.slide-chart .wide{position:absolute;left:18px;top:146px;width:292px}

.slide-pie{left:455px;top:770px}
.slide-pie .copy{position:absolute;left:24px;top:58px;width:190px}
.slide-pie .copy .para{text-align:center;margin-bottom:6px}
.slide-pie .pie{position:absolute;left:230px;top:54px;width:58px;height:58px}
.slide-pie .legend{position:absolute;left:230px;top:124px;font-family:var(--body);font-size:3.4px;color:#555;line-height:7px}
.slide-pie .legend i{display:inline-block;width:4px;height:4px;margin-right:4px;vertical-align:middle}
.slide-pie .legend p{margin-top:4px;line-height:5px}

.slide-thanks{left:801px;top:770px;background:var(--orange)}
.slide-thanks .big{position:absolute;top:16px;width:100%;text-align:center;font-family:var(--slab);font-weight:300;font-size:30px;color:var(--white)}
.slide-thanks .band{height:62px;border-top-color:var(--white);border-top-width:5px}
.slide-thanks .info{position:absolute;left:0;right:0;top:138px;text-align:center;color:var(--white);font-size:7px;line-height:8.5px;white-space:nowrap}
.slide-thanks .info .row{margin-top:6px;font-size:7.2px}
.slide-thanks .info .ico{display:inline-block;width:4px;height:4px;background:var(--orange);margin:0 3px;vertical-align:middle}
</style>
</head>
<body>
<div class="board">

  <!-- Business card front -->
  <section class="item card-front">
    <div class="name">Daniel Hartwell-Ames,<small>DMIN, PCC</small></div>
    <div class="roles">Owner | Trainer | Coach | Consultant</div>
    <div class="band"></div>
    <div class="contact" style="top:97px;font-size:5.8px;line-height:7px">Ridgeline Coaching &amp; Behavioral Consulting LLC<br>4821 Alder Crest Dr. Plano, TX 75024</div>
    <div class="contact" style="top:117px;font-size:5.4px"><span class="ico"></span>(555) 014-2290<span class="ico"></span>daniel@ridgelinecbc.com<span class="ico"></span>www.ridgelinecbc.com</div>
  </section>

  <!-- Business card back -->
  <section class="item card-back">
    <div class="brand">RIDGELINE</div>
    <div class="brand-sub">Coaching and Behavioral Consulting</div>
  </section>
  <div class="label" style="left:211px;top:524px">Businesscard</div>

  <!-- Letterhead -->
  <section class="item letterhead">
    <div class="logo">
      <div class="brand">RIDGELINE</div>
      <div class="brand-sub">Coaching and Behavioral Consulting</div>
    </div>
    <div class="greeting">Dear Mr. Smith,</div>
    <div class="body">
      <p>Lorem ipsum dolor sit amet, consectetur adipiscing elit. Donec orci purus, luctus vitae dignissim eu, iaculis sed purus. Vivamus faucibus, ipsum nec aliquet viverra, leo mauris condimentum ligula, sit amet sagittis enim ligula quis arcu. Nam egestas tortor id nisi porttitor mattis. In tortor ante, ultricies in suscipit a, tempus non massa. Vivamus et auctor mi. Fusce vel massa nulla. Phasellus nec eros mauris, et scelerisque orci.</p>
      <p>Donec malesuada orci vitae nulla accumsan porta a id massa. Quisque accumsan iaculis magna sit amet fringilla. Maecenas consequat, magna eget tincidunt semper, odio nibh rutrum mi, id feugiat ante nisi eu risus. Vestibulum nunc orci, rhoncus a placerat in, ultricies in mi. Cras mattis varius eros, vel fringilla nisi suscipit eget. Quisque scelerisque sagittis nulla at porttitor.</p>
      <p>Sed id augue vitae urna euismod commodo aliquet a quam. Pellentesque arcu velit, cursus et malesuada ut, consequat et diam. Nullam erat sem, rhoncus id ullamcorper vitae, rhoncus et arcu. In ultricies ultricies nulla, ut rutrum nisi iaculis at. Donec eu magna a metus ornare faucibus. Fusce aliquet faucibus ultricies. Morbi semper, est id tincidunt gravida, sem arcu adipiscing lacus, ac bibendum nulla leo eu purus. Quisque nec diam sed risus consectetur accumsan quis quis nibh. Vestibulum id purus lorem.</p>
      <p>It is a long established fact that a reader will be distracted by the readable content of a page when looking at its layout. The point of using Lorem Ipsum is that it has a more-or-less normal distribution of letters, as opposed to using 'Content here, content here', making it look like readable English. Many desktop publishing packages</p>
    </div>
    <div class="closing">Sincerely,</div>
    <div class="signer">Daniel Hartwell<small>CEO/ Founder</small></div>
    <div class="band"></div>
    <div class="contact" style="top:412px;font-size:5.8px;line-height:7px">Ridgeline Coaching &amp; Behavioral Consulting LLC<br>4821 Alder Crest Dr. Plano, TX 75024</div>
    <div class="contact" style="top:429px;font-size:5.8px"><span class="ico"></span>(555) 014-2290<span class="ico"></span>daniel@ridgelinecbc.com<span class="ico"></span>www.ridgelinecbc.com</div>
  </section>
  <div class="label" style="left:497px;top:531px">Letterhead</div>

  <!-- Notepads -->
  <section class="item pad pad-white">
    <div class="rings"></div>
    <div class="logo"><div class="brand">RIDGELINE</div><div class="brand-sub">Coaching and Behavioral Consulting</div></div>
    <div class="band"></div>
    <div class="url">www.ridgelinecbc.com</div>
  </section>
  <section class="item pad pad-orange">
    <div class="rings"></div>
    <div class="logo" style="top:48px"><div class="brand on-dark">RIDGELINE</div><div class="brand-sub on-dark">Coaching and Behavioral Consulting</div></div>
    <div class="band band-white"></div>
    <div class="url">www.ridgelinecbc.com</div>
  </section>
  <section class="item pad pad-lined">
    <div class="rings"></div>
    <div class="logo"><div class="brand">RIDGELINE</div><div class="brand-sub" style="font-size:2.6px">Coaching and Behavioral Consulting</div></div>
    <div class="lines"></div>
    <div class="url">www.ridgelinecbc.com</div>
  </section>
  <div class="label" style="left:902px;top:263px">Notepad</div>

  <!-- Envelope -->
  <section class="item env-back">
    <div class="flap"><span>www.ridgelinecbc.com</span></div>
  </section>
  <section class="item env-front">
    <div class="logo"><div class="brand">RIDGELINE</div><div class="brand-sub">Coaching and Behavioral Consulting</div></div>
    <div class="band"></div>
    <div class="addr">Ridgeline Coaching &amp; Behavioral Consulting LLC<br>4821 Alder Crest Dr. Plano, TX 75024</div>
  </section>
  <div class="label" style="left:870px;top:531px">Envelope</div>

  <!-- Slide: title -->
  <section class="item slide slide-title">
    <div class="sky" role="img" aria-label="Photograph of a snow-capped mountain peak at dusk"></div>
    <div class="slide-logo"><div class="brand on-dark">RIDGELINE</div><div class="brand-sub">Coaching and Behavioral Consulting</div></div>
    <div class="welcome"><div class="l1">Welcome to Our</div><div class="l2">PRESENTATION NAME</div><div class="l3">Description</div></div>
  </section>

  <!-- Slide: team -->
  <section class="item slide slide-team">
    <div class="head"></div>
    <div class="title">HEADING HERE</div>
    <div class="subtitle">Sub Heading</div>
    <div class="slide-logo"><div class="brand on-dark">RIDGELINE</div><div class="brand-sub">Coaching and Behavioral Consulting</div></div>
    <div class="member" style="left:19px"><div class="photo">Photo</div><div class="mname">Team member1</div><div class="mtitle">Title</div><div class="para">Lorem ipsum dolor sit amet, consectetur adipisicing elit, sed do eiusmod tempor incididunt</div></div>
    <div class="member" style="left:96px"><div class="photo">Photo</div><div class="mname">Team member2</div><div class="mtitle">Title</div><div class="para">ut labore et dolore magna aliqua. Ut enim ad minim veniam, quis nostrud exercitation</div></div>
    <div class="member" style="left:175px"><div class="photo">Photo</div><div class="mname">Team member3</div><div class="mtitle">Title</div><div class="para">ullamco laboris nisi ut aliquip ex ea commodo consequat. enim ad minim veniam,</div></div>
    <div class="member" style="left:251px"><div class="photo">Photo</div><div class="mname">Team member4</div><div class="mtitle">Title</div><div class="para">Do eiusmod tempor incididunt. Lorem ipsum dolor sit amet, consectetur adipiscing elit, sed</div></div>
    <div class="footer">www.ridgelinecbc.com<b>1</b></div>
  </section>

  <!-- Slide: photo and text -->
  <section class="item slide slide-meet">
    <div class="head"></div>
    <div class="title">HEADING HERE</div>
    <div class="subtitle">Sub Heading</div>
    <div class="slide-logo"><div class="brand">RIDGELINE</div><div class="brand-sub">Coaching and Behavioral Consulting</div></div>
    <div class="photo-area" role="img" aria-label="Photograph of business people shaking hands in a bright office"></div>
    <div class="copy">
      <h4>Heading</h4>
      <div class="para">Lorem ipsum dolor sit amet, consectetur adipisicing elit, sed do eiusmod tempor incididunt ut labore et dolore magna aliqua. Ut enim ad minim veniam, quis nostrud exercitation ullamco laboris nisi ut aliquip ex ea commodo consequat.</div>
      <h4>Heading</h4>
      <div class="para">Duis aute irure dolor in reprehenderit in voluptate velit esse cillum dolore eu fugiat nulla pariatur. Excepteur sint occaecat cupidatat non proident, sunt in culpa qui officia deserunt mollit anim id est laborum.</div>
      <h4>Heading</h4>
      <div class="para">Duis aute irure dolor in reprehenderit in voluptate velit esse cillum dolore eu fugiat nulla pariatur. Excepteur sint occaecat cupidatat non proident, sunt in culpa qui officia deserunt mollit anim id est laborum.</div>
    </div>
    <div class="footer">www.ridgelinecbc.com<b>3</b></div>
  </section>

  <!-- Slide: bar chart -->
  <section class="item slide slide-chart">
    <div class="head"></div>
    <div class="title">HEADING HERE</div>
    <div class="subtitle">Sub Heading</div>
    <div class="slide-logo"><div class="brand">RIDGELINE</div><div class="brand-sub">Coaching and Behavioral Consulting</div></div>
    <svg class="chart" viewBox="0 0 105 78" width="105" height="78" aria-label="Bar chart of four values">
      <g stroke="#d8d8d8" stroke-width=".4">
        <line x1="0" y1="2" x2="105" y2="2"/><line x1="0" y1="12" x2="105" y2="12"/><line x1="0" y1="22" x2="105" y2="22"/><line x1="0" y1="32" x2="105" y2="32"/><line x1="0" y1="42" x2="105" y2="42"/><line x1="0" y1="52" x2="105" y2="52"/><line x1="0" y1="62" x2="105" y2="62"/><line x1="0" y1="72" x2="105" y2="72"/>
      </g>
      <rect x="24" y="5" width="12.5" height="73" fill="var(--orange)"/>
      <rect x="40" y="15" width="12.5" height="63" fill="var(--orange)"/>
      <rect x="55.5" y="31" width="12.5" height="47" fill="var(--orange)"/>
      <rect x="72" y="20" width="12.5" height="58" fill="var(--orange)"/>
      <g fill="#fff" font-size="3.6" font-family="Jost, sans-serif">
        <text transform="translate(31.5 76) rotate(-90)">Sub text1</text>
        <text transform="translate(47.5 76) rotate(-90)">Sub text2</text>
        <text transform="translate(63 76) rotate(-90)">Sub text3</text>
        <text transform="translate(79.5 76) rotate(-90)">Sub text4</text>
      </g>
    </svg>
    <div class="copy">
      <div class="para">Sed ut perspiciatis unde omnis iste natus error sit voluptatem accusantium doloremque laudantium, totam rem aperiam, eaque ipsa quae ab illo inventore veritatis et quasi architecto beatae vitae dicta sunt explicabo. Nemo enim ipsam voluptatem quia voluptas sit aspernatur aut odit aut fugit, sed quia consequuntur magni dolores eos qui ratione voluptatem sequi nesciunt.</div>
      <div class="para">At vero eos et accusamus et iusto odio dignissimos ducimus qui blanditiis praesentium voluptatum deleniti atque corrupti quos dolores et quas molestias excepturi sint occaecati cupiditate non provident, similique sunt in culpa qui officia deserunt mollitia animi, id est laborum et dolorum fuga. Et harum quidem rerum facilis est et expedita distinctio.</div>
    </div>
    <div class="wide para">Lorem ipsum dolor sit amet, consectetur adipisicing elit, sed do eiusmod tempor incididunt ut labore et dolore magna aliqua. Ut enim ad minim veniam, quis nostrud exercitation ullamco laboris nisi ut aliquip ex ea commodo consequat. Duis aute irure dolor in reprehenderit in voluptate velit esse cillum dolore eu fugiat nulla pariatur. Excepteur sint occaecat cupidatat non proident.</div>
    <div class="footer">www.ridgelinecbc.com<b>3</b></div>
  </section>

  <!-- Slide: pie chart -->
  <section class="item slide slide-pie">
    <div class="head"></div>
    <div class="title">HEADING HERE</div>
    <div class="subtitle">Sub Heading</div>
    <div class="slide-logo"><div class="brand">RIDGELINE</div><div class="brand-sub">Coaching and Behavioral Consulting</div></div>
    <div class="copy">
      <div class="para">Lorem ipsum dolor sit amet, consectetur adipisicing elit, sed do eiusmod tempor incididunt ut labore et dolore magna aliqua. Ut enim ad minim veniam, quis nostrud exercitation ullamco laboris nisi ut aliquip ex ea commodo consequat. Duis aute irure dolor in reprehenderit in voluptate velit esse cillum dolore eu fugiat nulla pariatur.</div>
      <div class="para">Excepteur sint occaecat cupidatat non proident, sunt in culpa qui officia deserunt mollit anim id est laborum. Ut enim ad minim veniam, quis nostrud exercitation ullamco laboris nisi ut aliquip ex ea commodo consequat. At vero eos et accusamus et iusto odio dignissimos ducimus qui blanditiis praesentium voluptatum deleniti atque corrupti quos dolores et quas molestias.</div>
    </div>
    <svg class="pie" viewBox="-30 -30 60 60" width="58" height="58" aria-label="Pie chart with four segments">
      <circle r="29" fill="var(--orange)"/>
      <path d="M0 0 L0 -29 A29 29 0 0 1 27 -11Z" fill="var(--grey)" stroke="#fff" stroke-width=".8"/>
      <path d="M0 0 L29 1 A29 29 0 0 1 14 25Z" fill="var(--grey)" stroke="#fff" stroke-width=".8"/>
      <path d="M0 0 L27 -11 A29 29 0 0 1 29 1Z" fill="var(--orange)" stroke="#fff" stroke-width=".8"/>
    </svg>
    <div class="legend">
      <div><i style="background:var(--orange)"></i>Lorem ipsum dolor sit amet 50%</div>
      <div><i style="background:var(--grey)"></i>Duis aute irure dolor in 50%</div>
      <p>sunt in culpa qui officia deserunt mollit anim<br>id est laborum. Ut enim ad minim veniam</p>
    </div>
    <div class="footer">www.ridgelinecbc.com<b>5</b></div>
  </section>

  <!-- Slide: closing -->
  <section class="item slide slide-thanks">
    <div class="big">Thanks For Coming</div>
    <div class="band"></div>
    <div class="info">Ridgeline Coaching &amp; Behavioral Consulting LLC<br>4821 Alder Crest Dr. Plano, TX 75024
      <div class="row"><span class="ico"></span>(555) 014-2290 <span class="ico"></span>daniel@ridgelinecbc.com <span class="ico"></span>www.ridgelinecbc.com</div>
    </div>
  </section>
  <div class="label" style="left:603px;top:975px">Powerpoint &amp; Keynote</div>

</div>
</body>
</html>
```